Orchard sparkle graphic

We need a graphic for an offer in our dental office for Orchard sparkle treatment. Once enrolled the patient will be given a whitening treatment once a year for as long as they are a patient with our office. This means that they must come in for their routine cleanings. Fine print: There is an enrollment fee of 99 dollars and contact us for additional rules and conditions. We need a logo or picture that we can use on our home page slide show that is clean and makes you think of healthy white teeth. Our logo to our practice has been enclosed as well to give you style direction. We don't want this logo to have a ton of wording on it, it needs to be clean and modern looking. The name of the program is call Orchard Sparkle and we need to have the fine print on the ad as well, but we will be looking for entries that incorporate our logo that is submitted and can make this offer really stand out.

Dental

```html
<!DOCTYPE html>
<html lang="en">
<head>
<meta charset="utf-8">
<title>Orchard Sparkle – Harbor Point Dental Studio</title>
<link rel="stylesheet" href="https://fonts.googleapis.com/css2?family=Mulish:wght@200;300;400;600&display=swap">
<style>
  :root {
    --ink-deep: #0f3a3d;
    --ink-soft: #3d6466;
    --teal-light: #8dc6bc;
    --rule: #b9c2c2;
    --paper: #ffffff;
    --photo-light: #f3e3d8;
    --photo-deep: #e6c9b6;
  }
  html, body {
    margin: 0;
    padding: 0;
    overflow: hidden;
    background: var(--paper);
  }
  .banner {
    position: relative;
    width: 1200px;
    height: 408px;
    overflow: hidden;
    background: var(--paper);
    font-family: "Mulish", sans-serif;
  }
  .smile-photo {
    position: absolute;
    top: 0;
    right: 0;
    width: 455px;
    height: 408px;
    background: linear-gradient(90deg, var(--photo-light) 0%, var(--photo-deep) 100%);
  }
  .brand {
    position: absolute;
    left: 75px;
    top: 82px;
    color: var(--ink-deep);
  }
  .brand-name {
    display: flex;
    align-items: center;
    gap: 8px;
    font-size: 16px;
    font-weight: 600;
    margin: 0;
  }
  .brand-mark {
    width: 12px;
    height: 12px;
    background: var(--ink-deep);
  }
  .brand-doctors {
    margin: 3px 0 0 20px;
    font-size: 9px;
    font-weight: 600;
    letter-spacing: 0.2px;
  }
  .brand-doctors .divider {
    display: inline-block;
    width: 1px;
    height: 10px;
    background: var(--ink-deep);
    margin: 0 3px;
    vertical-align: -2px;
  }
  .headline {
    position: absolute;
    left: 68px;
    top: 172px;
    margin: 0;
    font-size: 62px;
    line-height: 1;
    letter-spacing: -0.5px;
  }
  .headline-light {
    font-weight: 200;
    color: var(--ink-soft);
  }
  .headline-strong {
    font-weight: 400;
    color: var(--ink-deep);
  }
  .fee {
    position: absolute;
    left: 69px;
    top: 306px;
    margin: 0;
    font-size: 19.5px;
    font-weight: 300;
    color: var(--teal-light);
  }
  .fee-rule {
    position: absolute;
    left: 0;
    top: 339px;
    width: 700px;
    height: 1px;
    background: linear-gradient(90deg, var(--rule) 0%, var(--rule) 80%, rgba(185,194,194,0) 100%);
  }
  .fine-print {
    position: absolute;
    left: 69px;
    top: 350px;
    margin: 0;
    font-size: 10.7px;
    font-weight: 400;
    line-height: 22px;
    color: var(--teal-light);
  }
</style>
</head>
<body>
  <div class="banner">
    <div class="smile-photo" role="img" aria-label="Close-up photo of a smile with bright white teeth"></div>

    <div class="brand">
      <p class="brand-name"><span class="brand-mark"></span>harbor point dental studio</p>
      <p class="brand-doctors">Dr Alan Whitford<span class="divider"></span>Dr Lena Cho</p>
    </div>

    <h1 class="headline"><span class="headline-light">orchard</span> <span class="headline-strong">sparkle</span></h1>

    <p class="fee">99 dollar enrollment fee</p>
    <div class="fee-rule"></div>

    <p class="fine-print">
      Once enrolled the patient will be given a whitening treatment once a year for as long as they are a patient with our office.<br>
      There is an enrollment fee of 99 dollars . Contact us for additional rules and conditions
    </p>
  </div>
</body>
</html>
```